Mobile technology Business Card Design Project

We need a business card design for our company based in Sydeny Australia, that takes a company's desktop sites and creates a mobile site compatible to all mobile/smartphone devices. This allows greater ease of use and generally faster business conversion than customers using a desktop site.
Our company is called Zelvora but we refer to it as Zelvora Solutions. If this could be represented somewhere on the business card that would be great.
Am open to suggestions regarding the colours but a high tech  theme would be good.
Happy bidding!

Target Market(s)
Business owner that has a website and is reasonably savvy regarding online/mobile marketing.
Industry/Entity Type
Business
Requirements
Must have
- Business card details:
Director Peter Hawkley
Address: 4/15 Brenton rd, Kelmore. 2047
Email: tbc
Web: www.zelvora-example.com.au
The cards need to have two different names for the two directors.
Damien Ferrowe & Peter Hawkley (two separate business cards)

```html
<!DOCTYPE html>
<html lang="en">
<head>
<meta charset="utf-8">
<title>Zelvora Business Card</title>
<link rel="stylesheet" href="https://fonts.googleapis.com/css2?family=Questrial&display=swap">
<style>
  :root {
    --backdrop: #4a2c1f;
    --card-light: #f7f7f7;
    --card-edge: #c6c6c8;
    --brand-blue: #3a90c2;
    --band-light: #55b4e2;
    --band-dark: #3a8cbe;
    --brand-orange: #f0962a;
    --ink: #222222;
    --white: #ffffff;
    --tagline-blue: #2a6e9c;
  }
  * { margin: 0; padding: 0; box-sizing: border-box; }
  html, body {
    width: 1200px; height: 1181px; overflow: hidden;
    background: var(--backdrop);
    font-family: "Questrial", sans-serif;
  }
  .canvas { position: relative; width: 1200px; height: 1181px; }
  .card {
    position: absolute; left: 232px; width: 734px; height: 422px;
    border-radius: 28px; overflow: hidden;
    background: radial-gradient(ellipse at 50% 45%, var(--card-light) 0%, #e6e6e7 45%, var(--card-edge) 100%);
  }
  .card--front { top: 127px; }
  .card--back { top: 621px; }
  .tab {
    position: absolute; left: 116px; width: 504px; height: 14px;
    background: var(--brand-blue);
  }
  .tab--top { top: 0; border-radius: 0 0 4px 4px; }
  .tab--bottom { bottom: 0; border-radius: 4px 4px 0 0; }

  .brand-mark {
    position: absolute; left: 295px; top: 100px;
    width: 146px; height: 146px; border-radius: 50%;
    background: var(--brand-blue);
  }
  .brand-name {
    position: absolute; left: 0; right: 0; top: 260px;
    text-align: center; font-size: 31px; color: var(--ink);
    letter-spacing: 1px;
  }
  .brand-tagline {
    position: absolute; left: 0; right: 0; top: 299px;
    text-align: center; font-size: 15px; color: var(--brand-orange);
    letter-spacing: 1px;
  }

  .info-band {
    position: absolute; left: 0; top: 77px; width: 100%; height: 268px;
    background: radial-gradient(ellipse at 48% 45%, var(--band-light) 0%, var(--band-dark) 100%);
  }
  .contact { position: absolute; left: 120px; top: 74px; color: var(--white); }
  .contact__name { font-size: 27px; line-height: 32px; }
  .contact__role { font-size: 21px; line-height: 24px; margin-bottom: 8px; }
  .contact__line { font-size: 15px; line-height: 21px; }
  .band-mark {
    position: absolute; left: 455px; top: 46px;
    width: 178px; height: 178px; border-radius: 50%;
    background: var(--white);
    display: flex; align-items: center; justify-content: center;
    color: var(--brand-blue); font-size: 28px;
  }
  .back-tagline {
    position: absolute; left: 0; right: 0; top: 385px;
    text-align: center; font-size: 15px; color: var(--tagline-blue);
  }
</style>
</head>
<body>
<main class="canvas">
  <section class="card card--front" aria-label="Card front">
    <div class="tab tab--top"></div>
    <div class="brand-mark"></div>
    <div class="brand-name">Zelvora</div>
    <div class="brand-tagline">Making Websites Mobile</div>
    <div class="tab tab--bottom"></div>
  </section>

  <section class="card card--back" aria-label="Card back">
    <div class="tab tab--top"></div>
    <div class="info-band">
      <div class="contact">
        <div class="contact__name">Peter Hawkley</div>
        <div class="contact__role">Director</div>
        <div class="contact__line">4/15 Brenton rd, Kelmore. 2047</div>
        <div class="contact__line">Yourname@zelvora-example.com</div>
        <div class="contact__line">www.zelvora-example.com.au</div>
      </div>
      <div class="band-mark">Zelvora</div>
    </div>
    <div class="back-tagline">Faster business conversion with Zelvora Solutions</div>
    <div class="tab tab--bottom"></div>
  </section>
</main>
</body>
</html>
```